Newly established winery needs label for its bottles

The Corvelle-Marsan Winery, is a small family owned winery that has been producing wine for little over 3 years. We are now ready to officially start commercializing our products. To do so we are looking for a label for our wine bottles. We are looking for a creative design that will differentiate our bottles from the more conventional labels. We are looking for one label design with 3 color schemes so that we can have a standard look and feel for all three of our wines, while having some differentiation between them with the different color schemes. In summary we are looking for a label that will standout by its uniqueness, simplicity and its modern touch. The label should also reflect the historical significance of the name of the winery. The attached documents offers more detail about the winery, what we are looking for, as well as some technical specification for the label. This label project is also related to a logo project see brief: http://www.pitchgallery.example/project-progress.aspx?briefId=553184). The logo project is now complete and the winning design source files were added to the documents in this brief. Also, details around the information that will need to appear on the label was added to the document list.
Updates
This label project will be on hold temporarily while the logo project is in progress. If you are interested in participating in the logo project, please follow this link: http://www.pitchgallery.example/project-progress.aspx?briefId=553184 Added Wednesday, December 17, 2014
Reason: Deadline extended to give sufficent time for submission and modification to the designs provided.

```html
<!DOCTYPE html>
<html lang="en">
<head>
<meta charset="utf-8">
<title>Corvelle-Marsan Wine Labels</title>
<link rel="stylesheet" href="https://fonts.googleapis.com/css2?family=Cormorant+Garamond:wght@500&family=Tinos&display=swap">
<style>
  :root {
    --page: #ffffff;
    --panel: #f1f4ee;
    --marble-light: #efe3cf;
    --marble-mid: #e2cfae;
    --marble-dark: #d4bd91;
    --vintage: #d7bf9e;
    --ink: #141414;
    --red-band: #5c0a12;
    --red-text: #d8bf98;
    --white-band: #d6bf9e;
    --rose-band: #fb857c;
  }
  * { margin: 0; padding: 0; box-sizing: border-box; }
  html, body { width: 1200px; height: 1000px; overflow: hidden; background: var(--page); }
  .canvas { position: relative; width: 1200px; height: 1000px; }
  .label {
    position: absolute; top: 277px; width: 384px; height: 458px;
    font-family: "Tinos", "Times New Roman", serif; color: var(--ink);
  }
  .label--red { left: 11px; }
  .label--white { left: 406px; }
  .label--rose { left: 801px; }
  .marble {
    position: absolute; left: 0; width: 100%;
    background: linear-gradient(115deg, var(--marble-light) 0%, var(--marble-mid) 35%, var(--marble-light) 55%, var(--marble-dark) 80%, var(--marble-light) 100%);
  }
  .marble--top { top: 0; height: 107px; }
  .marble--bottom { top: 397px; height: 61px; }
  .house-name {
    position: absolute; top: 0; left: 0; width: 100%; height: 107px;
    display: flex; align-items: center; justify-content: center;
    font-size: 26px; color: var(--ink); letter-spacing: 0.5px;
  }
  .panel { position: absolute; top: 107px; left: 0; width: 100%; height: 252px; background: var(--panel); overflow: hidden; }
  .vintage {
    position: absolute; top: 16px; left: 0; width: 100%; text-align: center;
    font-family: "Cormorant Garamond", Georgia, serif; font-weight: 500;
    font-size: 160px; line-height: 1; letter-spacing: -6px; color: var(--vintage);
  }
  .winery-name {
    position: absolute; left: 0; width: 100%; text-align: center;
    font-size: 28px; line-height: 1; white-space: nowrap;
  }
  .winery-name--en { top: 68px; }
  .winery-name--fr { top: 126px; }
  .origin { position: absolute; top: 169px; left: 65px; font-size: 11px; }
  .wine-type {
    position: absolute; top: 359px; left: 0; width: 100%; height: 38px;
    display: flex; align-items: center; justify-content: center;
    font-size: 17px; letter-spacing: -0.3px;
  }
  .label--red .wine-type { background: var(--red-band); color: var(--red-text); }
  .label--white .wine-type { background: var(--white-band); }
  .label--rose .wine-type { background: var(--rose-band); }
  .volume {
    position: absolute; top: 436px; left: 0; width: 100%; text-align: center;
    font-size: 11px; word-spacing: 3px;
  }
</style>
</head>
<body>
<main class="canvas">
  <section class="label label--red">
    <div class="marble marble--top" role="img" aria-label="Beige marble texture"></div>
    <div class="house-name">Corvelle-Marsan</div>
    <div class="panel">
      <div class="vintage">2015</div>
      <p class="winery-name winery-name--en">Winery Corvelle-Marsan</p>
      <p class="winery-name winery-name--fr">Vignoble Corvelle-Marsan</p>
      <p class="origin">Product of Québec / Produit du Québec</p>
    </div>
    <div class="wine-type">Red Wine / Vin Rouge</div>
    <div class="marble marble--bottom" role="img" aria-label="Beige marble texture"></div>
    <p class="volume">750 ml 11.6% alc./Vol.</p>
  </section>

  <section class="label label--white">
    <div class="marble marble--top" role="img" aria-label="Beige marble texture"></div>
    <div class="house-name">Corvelle-Marsan</div>
    <div class="panel">
      <div class="vintage">2015</div>
      <p class="winery-name winery-name--en">Winery Corvelle-Marsan</p>
      <p class="winery-name winery-name--fr">Vignoble Corvelle-Marsan</p>
      <p class="origin">Product of Québec / Produit du Québec</p>
    </div>
    <div class="wine-type">White Wine / Vin Blanc</div>
    <div class="marble marble--bottom" role="img" aria-label="Beige marble texture"></div>
    <p class="volume">750 ml 11.6% alc./Vol.</p>
  </section>

  <section class="label label--rose">
    <div class="marble marble--top" role="img" aria-label="Beige marble texture"></div>
    <div class="house-name">Corvelle-Marsan</div>
    <div class="panel">
      <div class="vintage">2015</div>
      <p class="winery-name winery-name--en">Winery Corvelle-Marsan</p>
      <p class="winery-name winery-name--fr">Vignoble Corvelle-Marsan</p>
      <p class="origin">Product of Québec / Produit du Québec</p>
    </div>
    <div class="wine-type">Rosé / Rosé</div>
    <div class="marble marble--bottom" role="img" aria-label="Beige marble texture"></div>
    <p class="volume">750 ml 11.6% alc./Vol.</p>
  </section>
</main>
</body>
</html>
```